Business Card Design Project

I need a new business card design for my building/development company: Kestrel Ridge Builders.

We specialise in small sub-divisions, multi-story developments and new house builds.
We handle the whole process from concept stage right throught to a fully developed property.
Updates

Target Market(s)

people looking to develop their property and need help. New property buyers

Industry/Entity Type

House

Requirements
Must have
• My logo on both sides:
Side 1: Logo taking up whole side as per old card but with a color/style change.

Side 2: Contact page: include logo but the rest just surprise me!

All contact details will be: (and need to be changable for each employee) I'll inform you of specifics before printing.

Name Surname
Position ie. Managing director
M: insert mobile
E: insert email
P.O. Box 518, Ashwell, Vic, 3094
www.kestrelridgebuilders.com.au

Nice to have
• Colors i'd like: (not necessarily all but this is the basic idea)

Black, blue, grey, silver, white

```html
<!DOCTYPE html>
<html lang="en">
<head>
<meta charset="utf-8">
<title>Kestrel Ridge Builders – Business Card</title>
<link rel="stylesheet" href="https://fonts.googleapis.com/css2?family=Open+Sans:wght@400;600;700&display=swap">
<style>
  :root {
    --backdrop: #e9e7e3;
    --card-dark: #36373b;
    --card-dark-deep: #2c2d31;
    --band-light: #f4f5f6;
    --band-silver: #d3d6da;
    --brand-blue: #1d7cc3;
    --text-white: #ffffff;
    --text-silver: #d6d8db;
    --text-ink: #1f2023;
    --divider: #8a8c90;
  }
  * { box-sizing: border-box; margin: 0; padding: 0; }
  html, body { width: 1200px; height: 880px; overflow: hidden; }
  body {
    background: var(--backdrop);
    font-family: "Open Sans", Arial, sans-serif;
    display: flex;
    align-items: center;
    justify-content: center;
    gap: 44px;
  }
  .card {
    position: relative;
    width: 520px;
    height: 318px;
    border-radius: 4px;
    overflow: hidden;
    box-shadow: 0 10px 28px rgba(0,0,0,0.25);
  }

  /* Contact side */
  .card--contact { background: var(--card-dark); }
  .contact-header {
    position: absolute;
    inset: 0 0 auto 0;
    height: 128px;
    background: linear-gradient(180deg, var(--band-light), var(--band-silver));
    display: flex;
    align-items: center;
    padding-left: 40px;
    gap: 16px;
  }
  .contact-header::after {
    content: "";
    position: absolute;
    left: 0; right: 0; bottom: -5px;
    height: 5px;
    background: var(--brand-blue);
  }
  .brand-square {
    width: 46px; height: 46px;
    background: var(--brand-blue);
    flex: none;
  }
  .brand-name {
    font-weight: 700;
    font-size: 27px;
    line-height: 1;
    color: var(--text-ink);
    letter-spacing: -0.2px;
  }
  .brand-tagline {
    margin-top: 5px;
    font-size: 12.5px;
    font-weight: 600;
    color: var(--text-ink);
    letter-spacing: 0.2px;
  }
  .contact-body {
    position: absolute;
    top: 133px; left: 0; right: 0; bottom: 0;
    display: flex;
    padding: 28px 24px 0 0;
  }
  .person {
    position: relative;
    width: 222px;
    padding-left: 40px;
    color: var(--text-white);
  }
  .person::before {
    content: "";
    position: absolute;
    left: 0; top: 4px;
    border-left: 12px solid var(--brand-blue);
    border-top: 9px solid transparent;
    border-bottom: 9px solid transparent;
  }
  .person-name { font-weight: 700; font-size: 15px; }
  .person-role { font-size: 15px; color: var(--text-silver); margin-top: 2px; }
  .divider {
    width: 1px;
    height: 130px;
    background: var(--divider);
    margin-right: 28px;
  }
  .details {
    list-style: none;
    color: var(--text-white);
    font-size: 14.5px;
    line-height: 1.6;
  }
  .details .gap { margin-top: 18px; }

  /* Logo side */
  .card--logo {
    background: radial-gradient(ellipse at 40% 40%, var(--card-dark), var(--card-dark-deep));
    display: flex;
    flex-direction: column;
    justify-content: center;
    padding-left: 60px;
  }
  .logo-lockup { display: flex; align-items: center; gap: 16px; }
  .logo-lockup .brand-square { width: 54px; height: 54px; }
  .card--logo .brand-name { color: var(--text-silver); font-size: 34px; }
  .card--logo .brand-tagline { color: var(--text-silver); font-size: 14px; font-weight: 400; margin-top: 7px; }
  .web-line {
    margin-top: 22px;
    margin-left: 70px;
    color: var(--text-silver);
    font-size: 15px;
    letter-spacing: 0.6px;
  }
</style>
</head>
<body>
  <section class="card card--contact" aria-label="Business card contact side">
    <header class="contact-header">
      <span class="brand-square" aria-hidden="true"></span>
      <div class="brand">
        <div class="brand-name">Kestrel Ridge Builders</div>
        <div class="brand-tagline">renovation-construction-development</div>
      </div>
    </header>
    <div class="contact-body">
      <div class="person">
        <div class="person-name">Name Surname</div>
        <div class="person-role">Managing director</div>
      </div>
      <div class="divider" aria-hidden="true"></div>
      <ul class="details">
        <li>0412 555 019</li>
        <li>name@kestrelridgebuilders.com.au</li>
        <li class="gap">P.O. Box 518, Ashwell, Vic, 3094</li>
        <li>www.kestrelridgebuilders.com.au</li>
      </ul>
    </div>
  </section>

  <section class="card card--logo" aria-label="Business card logo side">
    <div class="logo-lockup">
      <span class="brand-square" aria-hidden="true"></span>
      <div class="brand">
        <div class="brand-name">Kestrel Ridge Builders</div>
        <div class="brand-tagline">renovation-construction-development</div>
      </div>
    </div>
    <div class="web-line">www.kestrelridgebuilders.com.au</div>
  </section>
</body>
</html>
```